To create a website for KWRB Accounting and Tax Services

I want to create a website that has a compelling and clean home page, social media connections, some about information, services, pricing and a spot to do simple time bookings and a contact page. I have attached a sample pricing chart, and designs of my logo, business card and letterhead. KWRB Accounting and Tax Services is a small business in beautiful Niagara on the Lake which offers bookkeeping and tax services to the local residents and businesses. I would like the winning design that use the black and blue colour scheme from my stationary and should communicate a professional business that people can trust.

Target Market(s)

local residents who need their taxes prepared as well as small business who need bookkeeping services

Industry/Entity Type

Bookkeeper

Coding

Coded - Design and coding required

Number of Pages Required

5+ page

Font styles to use
Sans Serif

Requirements
Must have
• clean home page with hero images, about section (can be on home page), separate page for services, pricing, time slot booking and contact, social media connections including facebook page, twitter, linkedin,

```html
<!DOCTYPE html>
<html lang="en">
<head>
<meta charset="utf-8">
<title>KWRB Accounting and Tax Services</title>
<link href="https://fonts.googleapis.com/css2?family=Nunito+Sans:wght@300;400;600;700;800&family=Lato:wght@400;700;900&display=swap" rel="stylesheet">
<style>
:root{
  --black:#000;
  --panel:#1e1e1e;
  --blue:#1565c0;
  --blue-bright:#1e7be0;
  --blue-deep:#0b4fa8;
  --white:#fff;
  --grey:#c9c9c9;
}
*{box-sizing:border-box;margin:0;padding:0}
html,body{width:1200px;height:3182px;overflow:hidden;background:var(--black)}
body{position:relative;font-family:"Nunito Sans",sans-serif;color:var(--white)}
.abs{position:absolute}
.btn{position:absolute;display:flex;align-items:center;justify-content:center;background:linear-gradient(180deg,var(--blue-bright),var(--blue-deep));color:var(--white);font-family:"Lato",sans-serif;font-size:16px;font-weight:700;letter-spacing:.3px;text-transform:uppercase}
.rule{position:absolute;height:3px;width:60px;background:var(--blue-bright)}

/* header */
.site-header{position:absolute;left:0;top:0;width:1200px;height:108px;background:var(--black)}
.brand{position:absolute;left:150px;top:42px;display:flex;align-items:center;gap:12px;font-weight:700;font-size:17px;letter-spacing:2.5px;color:var(--white);text-transform:uppercase}
.brand-mark{width:14px;height:14px;background:var(--blue-bright)}
.phone-tab{position:absolute;left:815px;top:0;width:220px;height:40px}
.phone-tab span{position:absolute;left:32px;top:8px;font-family:"Lato",sans-serif;font-weight:700;font-size:20px;display:flex;align-items:center;gap:8px}
.main-nav{position:absolute;top:60px;left:577px;display:flex;gap:28px;font-family:"Lato",sans-serif;font-weight:700;font-size:15px}
.main-nav .active{position:relative}
.main-nav .active::after{content:"";position:absolute;left:0;right:0;top:44px;height:3px;background:var(--blue-bright)}

/* hero */
.hero{position:absolute;left:0;top:108px;width:1200px;height:564px;background:linear-gradient(100deg,#050505 0%,#1c1c1c 35%,#6d6d6d 65%,#b5b5b5 100%)}
.hero-frame{position:absolute;left:0;top:0}
.hero-kicker{position:absolute;left:187px;top:196px;font-size:27px;font-weight:600;color:var(--blue-bright)}
.hero-title{position:absolute;left:187px;top:228px;font-size:39px;font-weight:600;line-height:44px;letter-spacing:.3px}

/* about */
.about-title{position:absolute;left:0;width:1200px;top:738px;text-align:center;font-size:32px;font-weight:600;line-height:37px}
.about-copy{position:absolute;left:240px;width:720px;text-align:center;font-size:18px;font-weight:300;line-height:23px;color:#e6e6e6}

/* services */
.section-title{position:absolute;left:0;width:1200px;text-align:center;font-size:29px;font-weight:600}
.service-card{position:absolute;width:246px;height:291px}
.service-card h3{position:absolute;left:0;width:100%;top:64px;text-align:center;font-size:19px;font-weight:600}
.service-card p{position:absolute;left:30px;width:186px;top:102px;text-align:center;font-size:15.5px;font-weight:300;line-height:23px;color:var(--grey)}
.service-card .btn{left:45px;width:156px;height:39px;top:214px;font-size:15px}
.service-icon{position:absolute;top:-44px;left:85px}

/* pricing */
.plan{position:absolute;top:1867px;width:282px;height:541px;border:1px solid var(--blue-deep);background:var(--black)}
.plan-head{position:absolute;left:0;top:0;width:280px;height:130px;background:var(--panel)}
.plan-name{position:absolute;left:0;width:100%;top:28px;text-align:center;font-family:"Lato",sans-serif;font-weight:900;font-size:22px;color:var(--blue-bright)}
.plan-price{position:absolute;left:0;width:100%;top:58px;text-align:center;font-family:"Lato",sans-serif;font-size:33px;font-weight:900}
.plan-price small{font-size:23px;font-weight:400}
.features{position:absolute;left:26px;top:160px;width:232px;list-style:none;font-size:13.5px;line-height:15px}
.features li{position:relative;padding-left:19px;margin-bottom:14.7px}
.features li svg{position:absolute;left:0;top:1px}
.plan .btn{left:26px;top:475px;width:230px;height:39px}

/* booking */
.booking{position:absolute;left:0;top:2472px;width:1200px;height:520px;background:linear-gradient(90deg,#141414 0%,#1d1d1d 45%,#6a6a6a 80%,#8a8a8a 100%)}
.field{position:absolute;width:248px;height:48px;border:1px solid #6a6a6a;font-size:14px;color:#e0e0e0;display:flex;align-items:center;gap:8px;padding-left:19px}

/* footer */
.footer-nav{position:absolute;left:0;width:1200px;top:3021px;display:flex;justify-content:center;gap:31px;font-family:"Lato",sans-serif;font-weight:700;font-size:16px}
.copyright{position:absolute;left:0;width:1200px;top:3058px;text-align:center;font-size:13px}
.social{position:absolute;top:3090px;width:45px;height:45px;border-radius:50%;background:var(--blue)}
</style>
</head>
<body>
<svg width="0" height="0" style="position:absolute">
  <symbol id="tick" viewBox="0 0 14 14"><circle cx="7" cy="7" r="6" fill="none" stroke="#1e7be0" stroke-width="1.3"/><path d="M4 7.2l2 2 4-4.4" fill="none" stroke="#1e7be0" stroke-width="1.3"/></symbol>
</svg>

<header class="site-header">
  <div class="brand"><span class="brand-mark"></span>KWRB Accounting and Tax Services</div>
  <div class="phone-tab">
    <svg width="220" height="40"><polygon points="12,0 220,0 205,40 0,40" fill="#1565c0"/></svg>
    <span><svg width="17" height="17" viewBox="0 0 24 24"><path fill="#fff" d="M6.6 10.8a15 15 0 006.6 6.6l2.2-2.2c.3-.3.7-.4 1-.2 1.1.4 2.3.6 3.6.6.6 0 1 .4 1 1V20c0 .6-.4 1-1 1A17 17 0 013 4c0-.6.4-1 1-1h3.5c.6 0 1 .4 1 1 0 1.3.2 2.5.6 3.6.1.3 0 .7-.2 1z"/></svg>647-555-0192</span>
  </div>
  <nav class="main-nav"><span class="active">ABOUT</span><span>SERVICES</span><span>PRICING</span><span>BOOKING</span><span>CONTACT</span></nav>
</header>

<section class="hero" role="img" aria-label="Black and white photo of hands using a calculator and laptop over paperwork">
  <svg class="hero-frame" width="1200" height="564">
    <polyline points="167,363 147,363 147,157 563,157 563,363 375,363" fill="none" stroke="#1565c0" stroke-width="6"/>
    <polyline points="88,212 62,240 88,268" fill="none" stroke="#888" stroke-width="2"/>
    <polyline points="1107,212 1133,240 1107,268" fill="none" stroke="#333" stroke-width="2"/>
  </svg>
  <div class="hero-kicker">WELCOME TO KWRB</div>
  <div class="hero-title">ACCOUNTING AND<br>TAX SERVICES</div>
  <div class="btn" style="left:190px;top:338px;width:161px;height:40px">Learn More</div>
</section>

<section class="about">
  <h2 class="about-title">ABOUT KWRB ACCOUNTING<br>AND TAX SERVICES</h2>
  <div class="rule" style="left:571px;top:822px"></div>
  <p class="about-copy" style="top:847px">Nunc tempus felis vitae urna Vivamus porttitor neque at volutpat rutrum purus nisi eleifend libero a tempus libero lectus feugiat felis Morbi diam</p>
  <p class="about-copy" style="top:920px">mauris viverra in gravida eu mattis in ante Morbi eget arcu Morbi porta libero id ullamcorper nonummy nibh ligula pulvinar metus eget consectetuer augue nisi quis lacus Ut ac mi quis lacus mollis aliquam Curabitur iaculis</p>
  <div class="btn" style="left:522px;top:1022px;width:161px;height:40px">Learn More</div>
</section>

<section class="services">
  <svg class="abs" style="left:0;top:1130px" width="1200" height="620">
    <polygon points="0,75 150,75 595,5 1010,75 1200,75 1200,543 1010,543 595,613 150,543 0,543" fill="#262626" role="img" aria-label="Dark photo of a desk with keyboard and notebooks"/>
    <polyline points="0,75 150,75 595,5 1010,75 1200,75" fill="none" stroke="#1565c0" stroke-width="3"/>
    <polygon points="150,74 595,3 1010,74 595,10" fill="#1565c0"/>
    <polyline points="0,543 150,543 595,613 1010,543 1200,543" fill="none" stroke="#1565c0" stroke-width="3"/>
    <polygon points="150,544 595,615 1010,544 595,608" fill="#1565c0"/>
    <polyline points="160,306 136,335 160,364" fill="none" stroke="#aaa" stroke-width="2"/>
    <polyline points="1028,306 1052,335 1028,364" fill="none" stroke="#aaa" stroke-width="2"/>
  </svg>
  <h2 class="section-title" style="top:1200px">OUR SERVICES</h2>
  <div class="rule" style="left:572px;top:1248px"></div>

  <div class="service-card" style="left:199px;top:1323px">
    <svg class="abs" width="246" height="291"><polyline points="75,1 1,1 1,290 245,290 245,1 170,1" fill="none" stroke="#1565c0" stroke-width="3"/></svg>
    <svg class="service-icon" width="76" height="72" viewBox="0 0 76 72" fill="none" stroke="#fff" stroke-width="2"><rect x="3" y="26" width="34" height="42"/><path d="M8 34h24M8 44h24M8 54h24M16 34v30M24 34v30"/><rect x="32" y="2" width="30" height="52"/><path d="M37 10h20M37 16h20M37 22h20M37 28h20"/><rect x="46" y="18" width="26" height="50"/><path d="M59 48v14M55 52h7M55 58h7"/></svg>
    <h3>ACCOUNTING</h3>
    <p>Aulvinar metus eget consectetuer augue nisi quis lacus Ut ac mi quis lacus mollis</p>
    <div class="btn">Learn More</div>
  </div>

  <div class="service-card" style="left:478px;top:1323px">
    <svg class="abs" width="246" height="291"><polyline points="75,1 1,1 1,290 245,290 245,1 170,1" fill="none" stroke="#1565c0" stroke-width="3"/></svg>
    <svg class="service-icon" width="76" height="72" viewBox="0 0 76 72" fill="none" stroke="#fff" stroke-width="2"><rect x="8" y="4" width="58" height="48"/><rect x="14" y="10" width="46" height="36"/><path d="M37 52v10M24 66h26"/><circle cx="37" cy="30" r="8"/><path d="M22 24v-8M27 24v-6M47 24v-10M52 24v-6"/></svg>
    <h3>BOOKKEEPING</h3>
    <p>Aulvinar metus eget consectetuer augue nisi quis lacus Ut ac mi quis lacus mollis</p>
    <div class="btn">Learn More</div>
  </div>

  <div class="service-card" style="left:754px;top:1323px">
    <svg class="abs" width="246" height="291"><polyline points="75,1 1,1 1,290 245,290 245,1 170,1" fill="none" stroke="#1565c0" stroke-width="3"/></svg>
    <svg class="service-icon" width="76" height="72" viewBox="0 0 76 72" fill="none" stroke="#fff" stroke-width="2"><path d="M14 2h48v58l-10 10H14z"/><text x="38" y="20" fill="#fff" stroke="none" font-family="Lato,sans-serif" font-size="15" text-anchor="middle">TAX</text><path d="M22 30h32M22 38h32M22 46h20M22 54h20"/></svg>
    <h3 style="top:60px">TAX SERVICE</h3>
    <p style="top:98px">Aulvinar metus eget consectetuer augue nisi quis lacus Ut ac mi quis lacus mollis</p>
    <div class="btn" style="top:210px">Learn More</div>
  </div>
</section>

<section class="pricing">
  <h2 class="section-title" style="top:1791px;left:-7px">PRICING</h2>
  <div class="rule" style="left:564px;top:1836px"></div>

  <div class="plan" style="left:157px">
    <div class="plan-head"><div class="plan-name">Premium Plan</div><div class="plan-price">697<small>/month</small></div></div>
    <svg class="abs" style="left:0;top:110px" width="280" height="30"><path d="M0 20 Q70 6 140 18 T280 14 V30 H0z" fill="#000"/><path d="M0 20 Q70 6 140 18 T280 14" fill="none" stroke="#1e7be0" stroke-width="4"/></svg>
    <ul class="features">
      <li><svg width="14" height="14"><use href="#tick"/></svg>Transaction Volue (up to 200)</li>
      <li><svg width="14" height="14"><use href="#tick"/></svg>LedgerBooks Online: Essentials (Value $35)</li>
      <li><svg width="14" height="14"><use href="#tick"/></svg>LedgerBooks Online mobile app</li>
      <li><svg width="14" height="14"><use href="#tick"/></svg>Online Docusment Management App (Value $28)</li>
      <li><svg width="14" height="14"><use href="#tick"/></svg>Bank and Credit Card Reconciliations</li>
      <li><svg width="14" height="14"><use href="#tick"/></svg>Post Vendor Bills, Expenses and bank transctions</li>
      <li><svg width="14" height="14"><use href="#tick"/></svg>Sales Tax (HST/GST) Reconciliation</li>
      <li><svg width="14" height="14"><use href="#tick"/></svg>Unliited email and telephone support</li>
    </ul>
    <div class="btn">Get a Quote</div>
  </div>

  <div class="plan" style="left:461px">
    <div class="plan-head"><div class="plan-name">Plus</div><div class="plan-price">367<small>/month</small></div></div>
    <svg class="abs" style="left:0;top:110px" width="280" height="30"><path d="M0 20 Q70 6 140 18 T280 14 V30 H0z" fill="#000"/><path d="M0 20 Q70 6 140 18 T280 14" fill="none" stroke="#1e7be0" stroke-width="4"/></svg>
    <ul class="features">
      <li><svg width="14" height="14"><use href="#tick"/></svg>Transaction Volue (up to 100)</li>
      <li><svg width="14" height="14"><use href="#tick"/></svg>LedgerBooks Online: Essentials (Value $35)</li>
      <li><svg width="14" height="14"><use href="#tick"/></svg>LedgerBooks Online mobile app</li>
      <li><svg width="14" height="14"><use href="#tick"/></svg>Online Docusment Management App (Value $28)</li>
      <li><svg width="14" height="14"><use href="#tick"/></svg>Bank and Credit Card Reconciliations</li>
      <li><svg width="14" height="14"><use href="#tick"/></svg>Post Vendor Bills, Expenses and bank transctions</li>
      <li><svg width="14" height="14"><use href="#tick"/></svg>Sales Tax (HST/GST) Reconciliation</li>
      <li><svg width="14" height="14"><use href="#tick"/></svg>Unliited email and telephone support</li>
    </ul>
    <div class="btn">Get a Quote</div>
  </div>

  <div class="plan" style="left:765px">
    <div class="plan-head"><div class="plan-name">Entry</div><div class="plan-price">197<small>/month</small></div></div>
    <svg class="abs" style="left:0;top:110px" width="280" height="30"><path d="M0 20 Q70 6 140 18 T280 14 V30 H0z" fill="#000"/><path d="M0 20 Q70 6 140 18 T280 14" fill="none" stroke="#1e7be0" stroke-width="4"/></svg>
    <ul class="features">
      <li><svg width="14" height="14"><use href="#tick"/></svg>Transaction Volue (up to 50)</li>
      <li><svg width="14" height="14"><use href="#tick"/></svg>LedgerBooks Online: Essentials (Value $35)</li>
      <li><svg width="14" height="14"><use href="#tick"/></svg>LedgerBooks Online mobile app</li>
      <li><svg width="14" height="14"><use href="#tick"/></svg>Online Docusment Management App (Value $28)</li>
      <li><svg width="14" height="14"><use href="#tick"/></svg>Bank and Credit Card Reconciliations</li>
      <li><svg width="14" height="14"><use href="#tick"/></svg>Post Vendor Bills, Expenses and bank transctions</li>
      <li><svg width="14" height="14"><use href="#tick"/></svg>Sales Tax (HST/GST) Reconciliation</li>
      <li><svg width="14" height="14"><use href="#tick"/></svg>Unliited email and telephone support</li>
    </ul>
    <div class="btn">Get a Quote</div>
  </div>
</section>

<section class="booking" role="img" aria-label="Black and white photo of a smiling accountant working at an office desk">
  <svg class="abs" style="left:0;top:0" width="1200" height="520">
    <polygon points="0,452 150,452 595,520 1010,452 1200,452 1200,520 0,520" fill="#000"/>
    <polyline points="0,452 150,452 595,518 1010,452 1200,452" fill="none" stroke="#1565c0" stroke-width="3"/>
    <polygon points="150,451 595,520 1010,451 595,512" fill="#1565c0"/>
  </svg>
  <h2 class="abs" style="left:181px;top:73px;font-size:29px;font-weight:600">BOOKING FORM</h2>
  <div class="rule" style="left:181px;top:115px"></div>
  <div class="field" style="left:172px;top:141px">First Name</div>
  <div class="field" style="left:429px;top:141px">Last Name</div>
  <div class="field" style="left:172px;top:203px">Email address</div>
  <div class="field" style="left:429px;top:203px">Phone Number</div>
  <div class="field" style="left:172px;top:264px"><svg width="14" height="14" viewBox="0 0 14 14" fill="none" stroke="#ccc"><rect x="1" y="2.5" width="12" height="10.5"/><path d="M1 5.5h12M4 1v3M10 1v3M4 8h1M7 8h1M10 8h1M4 10.5h1M7 10.5h1"/></svg>Select Date</div>
  <div class="field" style="left:429px;top:264px"><svg width="16" height="16" viewBox="0 0 16 16" fill="none" stroke="#ddd" stroke-width="1.5"><circle cx="8" cy="8" r="6.5"/><path d="M8 4v4H5"/></svg>Select Time</div>
  <div class="btn" style="left:171px;top:331px;width:242px;height:43px;font-size:17px;font-weight:400">Book Now</div>
</section>

<footer>
  <nav class="footer-nav"><span>HOME</span><span>ABOUT</span><span>SERVICES</span><span>PRICING</span><span>BOOKING</span><span>CONTACT</span></nav>
  <p class="copyright">© 2019 Company Name  All right reserved</p>
  <span class="social" style="left:492px" aria-label="Social profile one"></span>
  <span class="social" style="left:547px" aria-label="Social profile two"></span>
  <span class="social" style="left:602px" aria-label="Social profile three"></span>
  <span class="social" style="left:657px" aria-label="Social profile four"></span>
</footer>
</body>
</html>
```